Banner Ad Design Project

I need a banner design. The website is under construction at www.brightmarrow.example

Name: Bright Marrow
Tagline: Steady Sparks for crowded calendars

This is a leadership development and executive coaching site. The past site is live at www.quillstepnow.example. (so you can get a sense of the content)

The audience are (BUSY) executives, senior managers, leaders and top professionals, so the feel needs to be highly professional but also modern and fresh. I want to communicate energy but also solid and trust worthy and not too new agey. The audience are also people with strong social values who want to change things - so not too corporate (Ie suits!)

I would like the design to be floating on a white background, very clean and simple. I am attracted to reds or sunset (burn orange crimson colors.) But totally open to any color ideas.
I am giving an open brief for your ideas.
Here are the dimensions 960px wide, roughly 190px height.

Reason: The weekend might give more time to designers to get involved. Thanks Vina

Hi designers

You may not have seen the additions I gave to this brief.

The banner should not have leader out front photo's. Maybe less corporate than I initially thought. 
Not too corporate (no suits!) Please no chess pieces, jigsaw pieces, cartoon images, cliche leadership images. 
Am am trying for inspiration /inspiring whilst still being professional. Very simple and clean.
Please can the design be floating in a white background so that the web page is borderless - A bit like it is in http://palmoriskel.example/
Thank you

Target Market(s)

Senior managers, executives but people who also want to change the world!

Industry/Entity Type

Construction

Requirements
Should not have
• Should not have leader out front photo's.
Maybe less corporate than I initially thought.
Am am trying for inspiration /inspiring whilst still being professional.
Please no chess pieces, jigsaw pieces, cartoon images, cliche leadership images. Not too corporate (Ie suits!)

Thanks

```html
<!DOCTYPE html>
<html lang="en">
<head>
<meta charset="utf-8">
<title>Bright Marrow banner</title>
<link rel="stylesheet" href="https://fonts.googleapis.com/css2?family=Arimo:ital,wght@0,700;1,400&display=swap">
<style>
  :root {
    --page-white: #ffffff;
    --brand-teal: #2ed3d8;
    --tagline-grey: #b9b9b9;
  }
  html, body {
    margin: 0;
    padding: 0;
    overflow: hidden;
    background: var(--page-white);
  }
  .banner {
    position: relative;
    width: 1200px;
    height: 238px;
    background: var(--page-white);
    overflow: hidden;
  }
  .brand-name {
    position: absolute;
    left: 185px;
    top: 30px;
    margin: 0;
    font-family: "Arimo", Arial, sans-serif;
    font-weight: 700;
    font-size: 104px;
    line-height: 1.15;
    letter-spacing: -1px;
    color: var(--brand-teal);
    white-space: nowrap;
  }
  .tagline {
    position: absolute;
    left: 288px;
    top: 164px;
    margin: 0;
    font-family: "Arimo", Arial, sans-serif;
    font-style: italic;
    font-weight: 400;
    font-size: 30px;
    line-height: 1.2;
    color: var(--tagline-grey);
    white-space: nowrap;
  }
</style>
</head>
<body>
  <header class="banner">
    <h1 class="brand-name">Bright Marrow</h1>
    <p class="tagline">Steady Sparks for crowded calendars</p>
  </header>
</body>
</html>
```